依頼詳細
依頼は、月刊誌「射心」の裏表紙デザインをお願い致します。弓道されている一般の方は、必ず目にする雑誌です。サイズは【左右154mm×天地232mm】です。尚、2018年10月号(10月1日発刊)に掲載予定です。

当社製品をメインに、シンプルかつ高級感のあるデザインを希望致します。
なんとなくあるイメージは、雑誌によく掲載されているハイブランドの広告のような物を想像していますが、それにとらわれず斬新なものでもかまいません。
ご参考に弊社ホームページをご覧下さい。

今回は「製品紹介」広告ではありませんので、あくまでも企業イメージの浸透をテーマに製作をお願い致します。

尚、素材はフェイスブックhttps://www.facebook.com/ayaseshagu-example/の写真から使用してください。

よろしくお願い致します。
記載項目
社名:有限会社 綾瀬射具工房
住所:〒810-0999 福岡市南区桜台7-14-3
電話番号:092-000-4137
FAX:092-000-4138
URL:http://www.ayaseshagu-example.com/
東洋射芸用品協会会員
弊社ロゴ
「初心者用から特註高級品まで」
希望イメージ
シンプル 複雑
単色 カラフル
暗い 明るい
日常 高級
遊び心 厳粛
未来的 伝統的
女性的 男性的
希望する色
納品ファイル
• イラストレーター形式 (.ai)
補足説明
納品物は
・イラストレータデータ(アウトライン済)
・jpgデータ

尚、採用されたデザインの著作権などの権利は、当社に帰属するようにお願致します。
過去当選作品を掲示させていただきます。ご参考になれば幸いです。
使用する写真についてのご指摘がありましたので、再度共有サイトにアップいたしました。こちらからご利用下さい。

http://photoshare-example.jp/ayaseshagu/1
■ 選んだ理由

構図、ロゴの配置、キャッチフレーズ等、弊社の要望であります「ハイブランド」をうまく体現した作品として、社内投票で1位となりました。

■ 提案者全員のお礼・コメント

前回に引き続き今回の募集でもたくさんの御応募いただきまして真にありがとうございます。

今回の作品もすべて秀逸で、色々考えてこられた作品でしたので、社内投票でもかなり票が割れました。今後もデザイン募集いたしますので、お見かけいただいた際は是非ご参加いただければありがたいです。

```html
<!DOCTYPE html>
<html lang="ja">
<head>
<meta charset="utf-8">
<title>綾瀬射具工房 裏表紙広告</title>
<link href="https://fonts.googleapis.com/css2?family=Shippori+Mincho:wght@400;600&family=Noto+Serif+JP:wght@400;600&display=swap" rel="stylesheet">
<style>
  :root {
    --ink: #2a2622;
    --ink-soft: #5a544d;
    --paper-light: #fbfaf8;
    --paper-mid: #ece8e3;
    --paper-edge: #d9d3cc;
    --strip: #151311;
    --mark: #1c1a18;
    --box-line: #9a948d;
    --photo-bow: #6d6a4e;
    --photo-leather: #a88463;
    --photo-glove-blue: #3c4a66;
    --photo-glove-red: #7e2a2a;
  }
  * { margin: 0; padding: 0; box-sizing: border-box; }
  html, body { width: 834px; height: 1200px; overflow: hidden; background: var(--paper-light); }
  .back-cover {
    position: relative;
    width: 834px;
    height: 1200px;
    background: radial-gradient(ellipse 70% 55% at 50% 38%, var(--paper-light) 0%, var(--paper-mid) 70%, var(--paper-edge) 100%);
    font-family: "Shippori Mincho", "Noto Serif JP", serif;
    color: var(--ink);
    text-align: center;
  }
  .tagline {
    position: absolute;
    top: 34px; left: 0; right: 0;
    font-size: 17px;
    letter-spacing: 0.55em;
    color: var(--ink-soft);
  }
  .brand-mark {
    position: absolute;
    top: 130px; left: 0; right: 0;
    height: 540px;
    display: flex;
    align-items: center;
    justify-content: center;
    gap: 28px;
  }
  .brand-mark .dot {
    flex: none;
    width: 96px; height: 96px;
    border-radius: 50%;
    background: var(--mark);
  }
  .brand-mark .name {
    font-size: 88px;
    font-weight: 600;
    letter-spacing: 0.06em;
    line-height: 1;
    color: var(--mark);
    white-space: nowrap;
  }
  .company {
    position: absolute;
    top: 680px; left: 0; right: 0;
  }
  .company .form { font-size: 17px; letter-spacing: 0.2em; }
  .company .name { font-size: 40px; letter-spacing: 0.16em; margin-top: 4px; font-weight: 600; }
  .company .member { font-size: 14px; letter-spacing: 0.1em; margin-top: 6px; color: var(--ink-soft); }
  .contact {
    position: absolute;
    top: 816px; left: 0; right: 0;
    font-size: 15px;
    font-style: normal;
    line-height: 1.75;
    letter-spacing: 0.04em;
  }
  .url {
    position: absolute;
    top: 878px; left: 0; right: 0;
    font-size: 15px;
    letter-spacing: 0.04em;
  }
  .search {
    position: absolute;
    top: 906px; left: 50%;
    transform: translateX(-50%);
    display: flex;
    align-items: center;
  }
  .search .field {
    width: 170px; height: 26px;
    border: 1px solid var(--box-line);
    background: #fff;
    font-size: 13px;
    line-height: 24px;
    letter-spacing: 0.1em;
  }
  .search .icon { width: 30px; height: 26px; display: flex; align-items: center; justify-content: center; }
  .photo-strip {
    position: absolute;
    top: 952px; left: 0; right: 0;
    height: 172px;
    background: var(--strip);
    display: grid;
    grid-template-columns: 1.15fr 1.15fr 1fr 1fr;
    gap: 6px;
    padding: 10px 0;
  }
  .photo { height: 100%; }
  .photo-bow { background: linear-gradient(120deg, #3f3d2e, var(--photo-bow) 60%, #c9c3b4); }
  .photo-leather { background: linear-gradient(140deg, #5c4330, var(--photo-leather) 55%, #d6bfa4); }
  .photo-glove-blue { background: radial-gradient(circle at 50% 55%, #d8cfbd 0%, var(--photo-glove-blue) 45%, #1a1a1c 85%); }
  .photo-glove-red { background: radial-gradient(circle at 50% 55%, #d9d2c6 0%, var(--photo-glove-red) 45%, #1a1a1c 85%); }
</style>
</head>
<body>
  <main class="back-cover">
    <p class="tagline">初心者用から特註高級品まで</p>

    <div class="brand-mark">
      <span class="dot"></span>
      <span class="name">綾瀬射具工房</span>
    </div>

    <section class="company">
      <p class="form">有限会社</p>
      <h1 class="name">綾瀬射具工房</h1>
      <p class="member">［ 東洋射芸用品協会会員 ］</p>
    </section>

    <address class="contact">
      〒810-0999 福岡市南区桜台7-14-3<br>
      Tel : 092-000-4137　Fax : 092-000-4138
    </address>

    <p class="url">http://www.ayaseshagu-example.com/</p>

    <div class="search">
      <div class="field">綾瀬射具工房</div>
      <div class="icon">
        <svg width="18" height="18" viewBox="0 0 18 18">
          <circle cx="7" cy="7" r="5" fill="none" stroke="#2a2622" stroke-width="2"/>
          <line x1="11" y1="11" x2="16" y2="16" stroke="#2a2622" stroke-width="2.4" stroke-linecap="round"/>
        </svg>
      </div>
    </div>

    <div class="photo-strip">
      <div class="photo photo-bow" role="img" aria-label="弓を手に取る職人の手元の写真"></div>
      <div class="photo photo-leather" role="img" aria-label="革を加工する職人の手仕事の写真"></div>
      <div class="photo photo-glove-blue" role="img" aria-label="紺色の弓懸の製品写真"></div>
      <div class="photo photo-glove-red" role="img" aria-label="赤い弓懸の製品写真"></div>
    </div>
  </main>
</body>
</html>
```